Web Design Project

We are looking for a new site design for the VELDO Conference & Expo. The current site can be found at
http://veldonorthsummit.example/
The URL is provided for reference. We want a completely different look and layout which is shown in the specifications document.
As part of the design, we want a home page, inside page and a mobile design. The mobile version is to be fairly simple and uncluttered and based on the web design - simple is key and a sample site is referenced in the specifications document.
The design you provide will be implemented in Joomla. The design winner will only need to provide the PSD or Fireworks PNG format. We anticipate creating the template coding in-house.
However, if you have experience creating Joomla templates, please let us know as we may ask you to bid separately to do that phase of the project.
We've provided a specifications document which includes wireframes of the home page, inside page, and mobile version as well as sample sites. We've also included logo files and a picture of the conference city.
For the header at the top, as indicated in the specs document, we want to keep the same overall treatment to every page. We don't want to include images from the city within the header. Instead we want a graphic treatment with the logo. In this manner, the design will be flexiable and can be used for future years.
For the home page, we've indicated that we'd like to have a banner placement implemented within the design. Please place the city image in this area with a nice graphic treatment. This might also be a good place to include the hosting city and date: Saskatoon, SK June 2-5. 2013
The wireframe is provided to illustrate the placement of content and menu items. The exact dimensions of each component can be revised as you see fit. We are also flexiable if you feel we have missed items.

```html
<!DOCTYPE html>
<html lang="en">
<head>
<meta charset="utf-8">
<title>VELDO Conference &amp; Expo</title>
<link href="https://fonts.googleapis.com/css2?family=PT+Sans:wght@400;700&family=Arimo&display=swap" rel="stylesheet">
<style>
:root{
  --blue:#1f5bb0;
  --blue-dark:#174a97;
  --blue-side:#1a70bd;
  --blue-box:#1b63ab;
  --blue-head:#1a5ca3;
  --field:#5a9ad4;
  --link:#6d8fc7;
  --text:#2454a8;
  --panel:#e9eef3;
  --footer:#dae3ea;
  --red:#c8272c;
  --white:#fff;
  --grey:#555;
}
*{margin:0;padding:0;box-sizing:border-box}
html,body{width:1200px;height:938px;overflow:hidden;background:#fff}
body{position:relative;font-family:"PT Sans",sans-serif;color:var(--text)}
.abs{position:absolute}
.logo{left:160px;top:52px;display:flex;align-items:center;gap:10px;font-size:34px;font-weight:700;color:var(--blue)}
.logo i{width:22px;height:22px;border-radius:50%;background:var(--blue);display:block}
.toplinks{left:866px;top:58px;display:flex;gap:16px;font-size:9.5px;color:var(--link)}
.toplinks span{display:flex;align-items:flex-end;gap:6px}
.search{left:862px;top:126px;width:188px;height:25px;display:flex;border:1px solid #ccc;border-radius:3px;overflow:hidden}
.search .field{flex:1;background:linear-gradient(#fff,#eee);font-size:12px;color:var(--link);padding:4px 11px;white-space:nowrap}
.go{background:var(--red);color:var(--white);font-size:12px;display:flex;align-items:center;justify-content:center;flex:none}
.search .go{width:33px}
.nav{left:150px;top:186px;width:900px;height:54px;border-radius:7px 7px 0 0;background:linear-gradient(#3b7ad2,var(--blue-dark));border-bottom:2px solid #0f3f86;display:flex;align-items:center;padding-left:37px}
.nav a{color:var(--white);text-decoration:none;font-size:13.5px;margin-right:38px}
.main{left:150px;top:249px;width:900px;height:506px;background:var(--panel);border-radius:6px 6px 0 0}
.side{left:150px;top:249px;width:221px;height:506px;background:var(--blue-side);border-radius:6px}
.box{position:absolute;left:14px;width:195px;background:var(--blue-box);border-radius:3px;overflow:hidden}
.box h3{background:var(--blue-head);height:30px;font-weight:400;font-size:12px;color:var(--white);display:flex;align-items:center;padding-left:34px;position:relative}
.box h3 svg{position:absolute;left:13px}
.mailbox{top:10px;height:107px}
.mailbox .email{position:absolute;left:11px;top:51px;width:174px;height:25px;display:flex;border-radius:3px;overflow:hidden}
.mailbox .email .field{flex:1;background:var(--field);color:var(--white);font-size:9.5px;line-height:25px;padding:0 11px;white-space:nowrap;overflow:hidden}
.mailbox .email .go{width:33px}
.quick{top:130px;height:210px}
.quick ul{list-style:none;padding-top:11px}
.quick li{font-size:11px;color:var(--white);height:28px;padding-left:39px;position:relative}
.quick li::before{content:"";position:absolute;left:16px;top:6px;width:4px;height:4px;border-radius:50%;background:#6ba8e0}
.cond{top:357px;height:137px}
.cond h3{height:43px;line-height:1.6}
.cond p{font-family:Arimo,sans-serif;font-size:11px;color:var(--white);padding:19px 0 0 14px;white-space:nowrap}
.join{position:absolute;left:14px;top:92px;width:101px;height:26px;background:var(--red);border-radius:3px;color:var(--white);font-size:13px;display:flex;align-items:center;padding-left:12px;gap:8px}
.banner{left:385px;top:259px;width:650px;height:255px;border-radius:5px;background:linear-gradient(#a9b4c4 0%,#d9c7a8 38%,#6f6752 55%,#4c5a3a 75%,#3b4a2e 100%)}
.dots{left:931px;top:284px;display:flex;gap:11px}
.dots i{width:13px;height:13px;border-radius:50%;background:#e8e8e8;display:block;border:1px solid #ccc}
.dots i.on{background:var(--red);border-color:#a11}
.welcome{left:385px;top:538px;font-size:14.5px;font-weight:400}
.copy{left:385px;top:566px;width:630px;font-size:10.2px;line-height:18.75px}
.copy p+p{margin-top:18.75px}
.footer{left:150px;top:755px;width:900px;height:128px;background:var(--footer);border-radius:0 0 7px 7px}
.follow{left:171px;top:777px;font-size:13.5px;color:#333}
.social{left:171px;top:822px;display:flex;gap:12px}
.social i{width:24px;height:24px;display:block}
.sponsors-title{left:384px;top:777px;font-size:13.5px;color:#333}
.sponsors{left:384px;top:812px;width:640px;height:48px;display:flex;justify-content:space-between;align-items:center}
.sponsors span{font-size:12px;font-weight:700;color:var(--blue-dark);display:flex;align-items:center;gap:5px}
.sponsors span i{width:10px;height:10px;border-radius:50%;background:var(--blue-dark);display:block}
.legal{left:150px;top:905px;font-size:9.5px;color:var(--grey)}
.footlinks{right:150px;top:905px;font-size:9.5px;color:var(--grey)}
</style>
</head>
<body>
<div class="abs logo"><i></i>VELDO</div>

<div class="abs toplinks">
  <span><svg width="16" height="16" viewBox="0 0 16 16"><path d="M1 8 8 1l7 7h-2v7H9v-4H7v4H3V8z" fill="#6d8fc7"/></svg>Home</span>
  <span><svg width="18" height="16" viewBox="0 0 18 16"><rect x="1" y="4" width="16" height="11" fill="none" stroke="#6d8fc7" stroke-width="1.5"/><path d="M1 4l8 6 8-6" fill="none" stroke="#6d8fc7" stroke-width="1.5"/></svg>Mail</span>
  <span><svg width="18" height="16" viewBox="0 0 18 16"><path d="M3 14c2-6 7-11 13-12l-1 3c-4 1-7 4-9 9z" fill="#6d8fc7"/></svg>Contact</span>
</div>

<div class="abs search"><span class="field">Search</span><span class="go">go</span></div>

<nav class="abs nav">
  <a>Home</a><a>About us</a><a>Schedule</a><a>Registration</a><a>exhibitors</a><a>Education</a><a>Sponsers</a><a>Connect</a>
</nav>

<div class="abs main"></div>

<aside class="abs side">
  <div class="box mailbox">
    <h3 style="padding-left:48px"><svg width="24" height="14" viewBox="0 0 24 14"><rect x="1" y="1" width="22" height="12" fill="none" stroke="#cfe3f7" stroke-width="1.5"/><path d="M1 1l11 7 11-7" fill="none" stroke="#cfe3f7" stroke-width="1.5"/></svg>Join Our Mails List</h3>
    <div class="email"><span class="field">Enter email here</span><span class="go">go</span></div>
  </div>
  <div class="box quick">
    <h3><svg width="6" height="10" viewBox="0 0 6 10"><path d="M0 0l6 5-6 5z" fill="#9cc3ea"/></svg>Quick Links</h3>
    <ul><li>Schedule</li><li>Registration</li><li>Exhibitors</li><li>Education</li><li>Sponsers</li><li>Connect</li></ul>
  </div>
  <div class="box cond">
    <h3><svg width="6" height="10" viewBox="0 0 6 10" style="top:8px"><path d="M0 0l6 5-6 5z" fill="#fff"/></svg>Current Conditions in<br>Conference City</h3>
    <p>veritatis et quasi architecto beat</p>
    <div class="join">Join Now <svg width="5" height="8" viewBox="0 0 5 8"><path d="M0 0l5 4-5 4z" fill="#fff"/></svg></div>
  </div>
</aside>

<div class="abs banner" role="img" aria-label="Photo of the conference city skyline at dusk with bridges over the river"></div>
<div class="abs dots"><i></i><i></i><i></i><i class="on"></i></div>

<h2 class="abs welcome">Welcome to Our Site</h2>
<div class="abs copy">
  <p>At vero eos et accusamus et iusto odio dignissimos ducimus qui blanditiis praesentium voluptatum deleniti atque corrupti quos dolores et quas molestias excepturi sint occaecati cupiditate non provident, similique sunt in culpa qui officia deserunt mollitia animi, ilillaborum et dolorum fuga. Et harum quidem rerum facilis est et expedita distinctio.</p>
  <p>&nbsp;Nam libero tempore, cum soluta nobis est eligendi optio cumque nihil impedit quo minus id quod maxime placeat facere possili, omnis voluptas assumenda est, omnis dolor repellendus. Temporibus autem quibusdam et aut officiis debitis aut rerum necessitatibus saepe eveniet ut et voluptates repudiandae sint et molestiae non recusandae. Itaque earum rerum hic tenetur a sapiente delectus, ut&nbsp; reiciendis voluptati-bus maiores alias consequatur aut perferendis doloribus asperiores repellat.</p>
</div>

<div class="abs footer"></div>
<div class="abs follow">Follow us on:</div>
<div class="abs social">
  <i style="background:#3b5b9a" title="Social 1"></i>
  <i style="background:#5cb8e6" title="Social 2"></i>
  <i style="background:#1c6fa8" title="Social 3"></i>
  <i style="background:#f08a24" title="Feed"></i>
</div>
<div class="abs sponsors-title">Our Sponsors</div>
<div class="abs sponsors">
  <span><i></i>Norvale</span>
  <span>Kestrel</span>
  <span>Ambrite</span>
  <span>Solvane</span>
  <span><i></i>Lumira</span>
  <span>Kestrel</span>
  <span>Ambrite</span>
</div>

<div class="abs legal">Copyright © 2012 veldonorthsummit.example. All Rights Reserved.</div>
<div class="abs footlinks">Home | About us | Schedule | Registration | exhibitors | Education | Sponsers | Connect</div>
</body>
</html>
```